Background on the company
=======================
This is a Bitcoin Consulting Company.

We have two projects.

Tinted Tokens: software to trade assets over the Bitcoin protocol (assets like property, traditional currencies, gold, stocks, securities, bonds, etc.).

Vaultrix Home Teller: a hardware based web service in a box that manages cold storage wallets and off line transaction signing. It is the secure way to deploy a web wallet without relying on third parties.

All that to say this is a high tech company focusing on Bitcoin.

What does Drellowmar mean?
========================

The Beast of Drellowmar is the rabbit in Quimby Larkets's Silver Goblet that defeats his band of knights. (At least until they go and get the Holy Hand Grenade).

We like this, because we are a deceptively soft and fuzzy company that is also killer!

What We Need:
============

Primarily we need to get the logo designed. I have a hand drawing I did, but you are not limited to that. And the logo needs to work on a business card. The right logo that works on a Business Card is the primary consideration.
Updates

The main task here is to get the logo right.  I have provided a drawing I made, and I like it, but my complaints are:  Drellowmar is hard to read.  The 'C' isn't obvious.

We can fix this many ways.  We can forget the whole "combinde a rabit with the C and a" idea.  We can add "Drellowmar Systems" on the card apart from the logo (that way if they don't "get it" they can still read it.)

The Rabbit itself is quite obviously scanned from a hand drawing.  That might not be a bad thing, but combine that with the entire logo, and it is too cheap looking.

Target Market(s)

Technical folks. Investors. Business contacts.

Industry/Entity Type

Software

Requirements
Must have
• We have to clean up the logo, or replace it with something that hints at the same sort of things. (See the upload) Basically and innocent white bunny. Something that works on a Business Card.

All the information below:

Derek Hale
ph (555) 314-9072
hale.derek@mailvora.net
derek@drellowmar.net
Nice to have
• I would like it to be serious, yet whimsical. An inside joke, so you get it if you know Quimby Larkets. But otherwise, it looks reasonably serious if you don't know Quimby Larkets.

I don't want it to be scary. (oddly, that my own efforts seem to make that easy to do)

Would like a set of colors that remind one of a cave, a rabbit, knights.... Not sure what those are...

```html
<!DOCTYPE html>
<html lang="en">
<head>
<meta charset="utf-8">
<title>Drellowmar Systems — Business Card</title>
<link rel="stylesheet" href="https://fonts.googleapis.com/css2?family=Open+Sans:wght@400;700&display=swap">
<style>
  :root {
    --backdrop: #d9d8d6;
    --card: #ffffff;
    --ink-dark: #1f1f1f;
    --ink-mid: #6e6e6e;
    --ink-soft: #8a8a8a;
  }
  html, body {
    margin: 0;
    padding: 0;
    width: 1200px;
    height: 900px;
    overflow: hidden;
    background: var(--backdrop);
  }
  .canvas {
    width: 1200px;
    height: 900px;
    display: flex;
    align-items: center;
    justify-content: center;
  }
  .business-card {
    position: relative;
    width: 1000px;
    height: 572px;
    background: var(--card);
    border-radius: 44px;
    box-shadow: 0 10px 30px rgba(0,0,0,0.12);
    font-family: "Open Sans", Arial, sans-serif;
  }
  .brand {
    position: absolute;
    top: 170px;
    left: 0;
    right: 0;
    display: flex;
    align-items: center;
    justify-content: center;
    gap: 14px;
  }
  .brand-dot {
    width: 18px;
    height: 18px;
    border-radius: 50%;
    background: var(--ink-dark);
  }
  .brand-name {
    font-weight: 700;
    font-size: 30px;
    letter-spacing: 3px;
    text-transform: uppercase;
    color: var(--ink-dark);
  }
  .contact-line {
    position: absolute;
    bottom: 110px;
    left: 0;
    right: 0;
    display: flex;
    align-items: center;
    justify-content: center;
    gap: 26px;
    font-size: 17px;
    color: var(--ink-mid);
  }
  .contact-name {
    font-weight: 700;
    color: var(--ink-soft);
  }
  .contact-item {
    display: flex;
    align-items: center;
    gap: 6px;
  }
  .contact-icon {
    width: 16px;
    height: 16px;
    fill: var(--ink-mid);
  }
</style>
</head>
<body>
<main class="canvas">
  <section class="business-card">
    <div class="brand">
      <span class="brand-dot"></span>
      <span class="brand-name">Drellowmar Systems</span>
    </div>
    <div class="contact-line">
      <span class="contact-name">Derek Hale</span>
      <span class="contact-item">
        <svg class="contact-icon" viewBox="0 0 24 24" aria-hidden="true">
          <path d="M6.6 10.8a15.1 15.1 0 0 0 6.6 6.6l2.2-2.2a1 1 0 0 1 1-.25 11.4 11.4 0 0 0 3.6.57 1 1 0 0 1 1 1V20a1 1 0 0 1-1 1A17 17 0 0 1 3 4a1 1 0 0 1 1-1h3.5a1 1 0 0 1 1 1c0 1.25.2 2.45.57 3.57a1 1 0 0 1-.25 1z"/>
        </svg>
        (555) 314-9072
      </span>
      <span class="contact-item">
        <svg class="contact-icon" viewBox="0 0 24 24" aria-hidden="true">
          <path d="M2 5h20v14H2z M3.5 6.5 12 13l8.5-6.5" fill="none" stroke="currentColor"/>
          <path d="M2 5h20v14H2V5zm1.8 1.5L12 12.6l8.2-6.1H3.8z"/>
        </svg>
        hale.derek@mailvora.net
      </span>
      <span class="contact-item">derek@drellowmar.net</span>
    </div>
  </section>
</main>
</body>
</html>
```